I would like to modify/update my 2 step login screen

I want a more modern looking login page for our document imaging application. I need to keep all of the same elements and buttons that currently exist. The first 2 screens are the login. The 3rd is a screenshot of the actual application home page.

```html
<!DOCTYPE html>
<html lang="en">
<head>
<meta charset="utf-8">
<title>Meridian Docs – Classic Login States</title>
<link href="https://fonts.googleapis.com/css2?family=Inter:wght@400;500;600;700&display=swap" rel="stylesheet">
<style>
  :root{
    --canvas:#f0f0f0;
    --brand-dark:#3b3c3e;
    --white:#ffffff;
    --ink:#2b2b2b;
    --muted:#9a9a9a;
    --line:#dcdcdc;
    --green:#5cb85c;
    --red:#e06464;
    --disabled:#c6c6c6;
    --notice-bg:#f6f6f6;
    --lock-blue:#3a7bd5;
  }
  html,body{margin:0;width:1200px;height:482px;overflow:hidden;background:var(--canvas);font-family:"Inter",Arial,sans-serif;}
  .board{position:absolute;left:0;top:0;width:2576px;height:1036px;transform:scale(0.46584);transform-origin:0 0;}
  .screen{position:absolute;width:796px;height:447px;background:var(--white);overflow:hidden;}
  .brand-panel{position:absolute;left:0;top:0;width:349px;height:447px;background:var(--brand-dark);color:var(--white);text-align:center;}
  .brand-name{position:absolute;left:0;right:0;top:216px;margin:0;font-size:22px;font-weight:700;letter-spacing:1px;display:flex;justify-content:center;align-items:center;gap:10px;}
  .brand-mark{width:16px;height:16px;border-radius:50%;background:var(--white);}
  .legal-links{position:absolute;left:0;right:0;top:399px;font-size:7px;font-weight:500;}
  .legal-links span{margin:0 4px;}
  .copyright{position:absolute;left:0;right:0;top:414px;margin:0;font-size:6.5px;color:#9c9c9c;}
  .login-panel{position:absolute;left:349px;top:0;width:447px;height:447px;}
  .error-banner{position:absolute;left:0;top:0;width:447px;height:23px;background:var(--red);color:var(--white);font-size:7.5px;display:flex;align-items:center;justify-content:center;}
  .method-tabs{position:absolute;left:107px;top:63px;width:233px;height:27px;display:flex;border-bottom:1px solid var(--line);}
  .method-tab{flex:1;display:flex;align-items:center;justify-content:center;}
  .method-tab.is-active{border-bottom:2px solid var(--green);margin-bottom:-1px;}
  .tab-dot{width:9px;height:9px;border-radius:50%;background:#b9b9b9;}
  .tab-square{width:9px;height:9px;background:#b9b9b9;}
  .tab-dot.dark{background:#1e1e1e;}
  .login-title{position:absolute;left:107px;top:118px;margin:0;font-size:14px;font-weight:600;color:var(--ink);}
  .field{position:absolute;left:107px;width:233px;height:25px;box-sizing:border-box;border:1px solid var(--line);border-radius:3px;display:flex;align-items:center;padding:0 7px;gap:6px;font-size:7.5px;color:var(--ink);}
  .field.is-focused{border-color:var(--green);}
  .field.is-invalid{border-color:var(--red);}
  .field svg{width:11px;height:11px;flex:none;}
  .field .value{flex:1;}
  .field .placeholder{flex:1;color:var(--muted);}
  .field .caret{display:inline-block;width:1px;height:9px;background:var(--ink);vertical-align:middle;}
  .field .dots{flex:1;font-size:9px;letter-spacing:1px;}
  .field .aux{width:9px;height:9px;}
  .field .sep{width:1px;height:11px;background:var(--line);}
  .action-button{position:absolute;left:107px;width:233px;height:22px;border:none;border-radius:2px;color:var(--white);font-family:inherit;font-size:7.5px;font-weight:600;display:flex;align-items:center;justify-content:center;}
  .action-button.is-disabled{background:var(--disabled);}
  .action-button.is-ready{background:var(--green);}
  .database-row{position:absolute;left:107px;top:163px;display:flex;align-items:center;gap:8px;font-size:7.5px;color:#777;}
  .database-row svg{width:10px;height:10px;}
  .database-row .divider{width:1px;height:11px;background:var(--line);}
  .database-row b{font-weight:500;color:#555;}
  .forgot-link{position:absolute;left:107px;top:280px;font-size:7.5px;font-weight:500;color:var(--green);}
  .activity-notice{position:absolute;left:0;top:422px;width:447px;height:25px;background:var(--notice-bg);border-top:1px solid #e8e8e8;font-size:6.5px;color:#555;display:flex;align-items:center;justify-content:center;}
  .activity-notice b{font-weight:600;color:#333;}
</style>
</head>
<body>
<svg width="0" height="0" style="position:absolute">
  <defs>
    <symbol id="i-db" viewBox="0 0 12 12"><rect x="1" y="1.5" width="10" height="4" rx="1" fill="none" stroke="#555" stroke-width="1"/><rect x="1" y="6.5" width="10" height="4" rx="1" fill="none" stroke="#555" stroke-width="1"/></symbol>
    <symbol id="i-user" viewBox="0 0 12 12"><circle cx="6" cy="4" r="2.5" fill="none" stroke="#555"/><path d="M1.5 11c0-2.6 2-4 4.5-4s4.5 1.4 4.5 4" fill="none" stroke="#555"/></symbol>
    <symbol id="i-lock" viewBox="0 0 12 12"><rect x="2" y="5.5" width="8" height="5.5" rx="1" fill="none" stroke="#555"/><path d="M4 5.5V4a2 2 0 0 1 4 0v1.5" fill="none" stroke="#555"/></symbol>
    <symbol id="i-lock-tab" viewBox="0 0 12 12"><rect x="2" y="5" width="8" height="6" rx="1" fill="#3a7bd5"/><path d="M4 5V3.6a2 2 0 0 1 4 0V5" fill="none" stroke="#3a7bd5" stroke-width="1.3"/></symbol>
    <symbol id="i-clear" viewBox="0 0 12 12"><circle cx="6" cy="6" r="5" fill="none" stroke="#888"/><path d="M4 4l4 4M8 4l-4 4" stroke="#888"/></symbol>
    <symbol id="i-eye" viewBox="0 0 12 12"><path d="M1 6s2-3.5 5-3.5S11 6 11 6 9 9.5 6 9.5 1 6 1 6z" fill="none" stroke="#888"/><circle cx="6" cy="6" r="1.5" fill="none" stroke="#888"/><path d="M2 10L10 2" stroke="#888"/></symbol>
    <symbol id="i-back" viewBox="0 0 12 12"><path d="M10 6H2M5 3L2 6l3 3" fill="none" stroke="#999"/></symbol>
  </defs>
</svg>

<main class="board">

  <!-- Step 1: empty database -->
  <section class="screen" style="left:47px;top:47px">
    <div class="brand-panel">
      <p class="brand-name"><span class="brand-mark"></span>MERIDIAN DOCS</p>
      <nav class="legal-links">Privacy<span>•</span>Remote Support<span>•</span>Contact Us</nav>
      <p class="copyright">Copyright 2007-2024 Meridian Docs</p>
    </div>
    <div class="login-panel">
      <div class="method-tabs">
        <div class="method-tab is-active"><svg width="10" height="10"><use href="#i-lock-tab"/></svg></div>
        <div class="method-tab"><span class="tab-dot"></span></div>
        <div class="method-tab"><span class="tab-square"></span></div>
        <div class="method-tab"><span class="tab-dot dark"></span></div>
      </div>
      <h1 class="login-title">Classic Login</h1>
      <div class="field" style="top:165px"><svg><use href="#i-db"/></svg><span class="placeholder">Database</span></div>
      <div class="action-button is-disabled" style="top:204px">NEXT</div>
      <footer class="activity-notice">All activity on this site is being recorded. Your IP Address is being saved as '<b>192.168.168.134</b>'.</footer>
    </div>
  </section>

  <!-- Step 1: typing database -->
  <section class="screen" style="left:890px;top:47px">
    <div class="brand-panel">
      <p class="brand-name"><span class="brand-mark"></span>MERIDIAN DOCS</p>
      <nav class="legal-links">Privacy<span>•</span>Remote Support<span>•</span>Contact Us</nav>
      <p class="copyright">Copyright 2007-2024 Meridian Docs</p>
    </div>
    <div class="login-panel">
      <div class="method-tabs">
        <div class="method-tab is-active"><svg width="10" height="10"><use href="#i-lock-tab"/></svg></div>
        <div class="method-tab"><span class="tab-dot"></span></div>
        <div class="method-tab"><span class="tab-square"></span></div>
        <div class="method-tab"><span class="tab-dot dark"></span></div>
      </div>
      <h1 class="login-title">Classic Login</h1>
      <div class="field is-focused" style="top:165px"><svg><use href="#i-db"/></svg><span class="value">ABC12345<span class="caret"></span></span><svg class="aux"><use href="#i-clear"/></svg></div>
      <div class="action-button is-disabled" style="top:204px">NEXT</div>
      <footer class="activity-notice">All activity on this site is being recorded. Your IP Address is being saved as '<b>192.168.168.134</b>'.</footer>
    </div>
  </section>

  <!-- Step 1: invalid database -->
  <section class="screen" style="left:1733px;top:47px">
    <div class="brand-panel">
      <p class="brand-name"><span class="brand-mark"></span>MERIDIAN DOCS</p>
      <nav class="legal-links">Privacy<span>•</span>Remote Support<span>•</span>Contact Us</nav>
      <p class="copyright">Copyright 2007-2024 Meridian Docs</p>
    </div>
    <div class="login-panel">
      <div class="error-banner">Invalid database. Please enter the correct data and try again.</div>
      <div class="method-tabs">
        <div class="method-tab is-active"><svg width="10" height="10"><use href="#i-lock-tab"/></svg></div>
        <div class="method-tab"><span class="tab-dot"></span></div>
        <div class="method-tab"><span class="tab-square"></span></div>
        <div class="method-tab"><span class="tab-dot dark"></span></div>
      </div>
      <h1 class="login-title">Classic Login</h1>
      <div class="field is-invalid" style="top:165px"><svg><use href="#i-db"/></svg><span class="value">ABC12345XYZ</span><svg class="aux"><use href="#i-clear"/></svg></div>
      <div class="action-button is-ready" style="top:204px">NEXT</div>
      <footer class="activity-notice">All activity on this site is being recorded. Your IP Address is being saved as '<b>192.168.168.134</b>'.</footer>
    </div>
  </section>

  <!-- Step 2: empty credentials -->
  <section class="screen" style="left:47px;top:542px">
    <div class="brand-panel">
      <p class="brand-name"><span class="brand-mark"></span>MERIDIAN DOCS</p>
      <nav class="legal-links">Privacy<span>•</span>Remote Support<span>•</span>Contact Us</nav>
      <p class="copyright">Copyright 2007-2024 Meridian Docs</p>
    </div>
    <div class="login-panel">
      <div class="method-tabs">
        <div class="method-tab is-active"><svg width="10" height="10"><use href="#i-lock-tab"/></svg></div>
        <div class="method-tab"><span class="tab-dot"></span></div>
        <div class="method-tab"><span class="tab-square"></span></div>
        <div class="method-tab"><span class="tab-dot dark"></span></div>
      </div>
      <h1 class="login-title">Classic Login</h1>
      <div class="database-row"><svg><use href="#i-back"/></svg><span class="divider"></span><svg><use href="#i-db"/></svg><span>Database : <b>ABC12345</b></span></div>
      <div class="field" style="top:206px"><svg><use href="#i-user"/></svg><span class="placeholder">Username</span></div>
      <div class="field" style="top:238px"><svg><use href="#i-lock"/></svg><span class="placeholder">Password</span><svg class="aux"><use href="#i-eye"/></svg></div>
      <div class="forgot-link">Forgot Password?</div>
      <div class="action-button is-disabled" style="top:305px">LOGIN</div>
      <footer class="activity-notice">All activity on this site is being recorded. Your IP Address is being saved as '<b>192.168.168.134</b>'.</footer>
    </div>
  </section>

  <!-- Step 2: typing credentials -->
  <section class="screen" style="left:890px;top:542px">
    <div class="brand-panel">
      <p class="brand-name"><span class="brand-mark"></span>MERIDIAN DOCS</p>
      <nav class="legal-links">Privacy<span>•</span>Remote Support<span>•</span>Contact Us</nav>
      <p class="copyright">Copyright 2007-2024 Meridian Docs</p>
    </div>
    <div class="login-panel">
      <div class="method-tabs">
        <div class="method-tab is-active"><svg width="10" height="10"><use href="#i-lock-tab"/></svg></div>
        <div class="method-tab"><span class="tab-dot"></span></div>
        <div class="method-tab"><span class="tab-square"></span></div>
        <div class="method-tab"><span class="tab-dot dark"></span></div>
      </div>
      <h1 class="login-title">Classic Login</h1>
      <div class="database-row"><svg><use href="#i-back"/></svg><span class="divider"></span><svg><use href="#i-db"/></svg><span>Database : <b>ABC12345</b></span></div>
      <div class="field" style="top:206px"><svg><use href="#i-user"/></svg><span class="value">JohnDoe123</span><svg class="aux"><use href="#i-clear"/></svg></div>
      <div class="field is-focused" style="top:238px"><svg><use href="#i-lock"/></svg><span class="dots">●●●<span class="caret"></span></span><svg class="aux"><use href="#i-eye"/></svg><span class="sep"></span><svg class="aux"><use href="#i-clear"/></svg></div>
      <div class="forgot-link">Forgot Password?</div>
      <div class="action-button is-ready" style="top:305px">LOGIN</div>
      <footer class="activity-notice">All activity on this site is being recorded. Your IP Address is being saved as '<b>192.168.168.134</b>'.</footer>
    </div>
  </section>

  <!-- Step 2: invalid credentials -->
  <section class="screen" style="left:1733px;top:542px">
    <div class="brand-panel">
      <p class="brand-name"><span class="brand-mark"></span>MERIDIAN DOCS</p>
      <nav class="legal-links">Privacy<span>•</span>Remote Support<span>•</span>Contact Us</nav>
      <p class="copyright">Copyright 2007-2024 Meridian Docs</p>
    </div>
    <div class="login-panel">
      <div class="error-banner">Invalid username and/or password. Please enter the correct data and try again.</div>
      <div class="method-tabs">
        <div class="method-tab is-active"><svg width="10" height="10"><use href="#i-lock-tab"/></svg></div>
        <div class="method-tab"><span class="tab-dot"></span></div>
        <div class="method-tab"><span class="tab-square"></span></div>
        <div class="method-tab"><span class="tab-dot dark"></span></div>
      </div>
      <h1 class="login-title">Classic Login</h1>
      <div class="database-row"><svg><use href="#i-back"/></svg><span class="divider"></span><svg><use href="#i-db"/></svg><span>Database : <b>ABC12345</b></span></div>
      <div class="field is-invalid" style="top:206px"><svg><use href="#i-user"/></svg><span class="value">johndoe</span><svg class="aux"><use href="#i-clear"/></svg></div>
      <div class="field is-invalid" style="top:238px"><svg><use href="#i-lock"/></svg><span class="dots">●●●●●●</span><svg class="aux"><use href="#i-eye"/></svg><span class="sep"></span><svg class="aux"><use href="#i-clear"/></svg></div>
      <div class="forgot-link">Forgot Password?</div>
      <div class="action-button is-ready" style="top:305px">LOGIN</div>
      <footer class="activity-notice">All activity on this site is being recorded. Your IP Address is being saved as '<b>192.168.168.134</b>'.</footer>
    </div>
  </section>

</main>
</body>
</html>
```